Cradlekin by Marianne Business Card Design

i am starting a new business as a reborn artist (that is painting dolls to make them look like real live babies)

i eventually want to sell the dolls that i make and have classed in reborning. but at the moment i just want to get my name out there.

I do not currently have images of the dolls so cannot have an image in the design.

Non compulsory thoughts: i like the look of old wood, white and baby pink,even hot pink, and lace, denim. i had in mind something like a tiny baby in a old cradle or something, a old drawer, box, something different or unusual, it has to be a girl baby. i am also open to other thoughts on the matter. i would like plain writing not all swirly
Updates

Sorry to change but would like it to read country cradlekin by marianne.

Reason: I have not been able to find the design I am looking for

Industry/Entity Type

Painting

Contact Information for Business Card

Cradlekin by Marianne
country babies that never grow up
Reborn Artist Marianne Holt
0437 651 840
lunet.v@mailvane.net

```html
<!DOCTYPE html>
<html lang="en">
<head>
<meta charset="utf-8">
<title>Cradlekin by Marianne – Business Card</title>
<link rel="stylesheet" href="https://fonts.googleapis.com/css2?family=Parisienne&family=Italianno&family=Raleway:wght@400;700&display=swap">
<style>
  :root {
    --backdrop: #e8e9ea;
    --card: #ffffff;
    --ink: #2a2a2a;
    --pink: #e2407c;
    --pink-soft: #eea3bf;
    --rose: #c4567d;
    --maroon: #4e1f2e;
    --lace: #f3f0f1;
  }
  * { box-sizing: border-box; margin: 0; padding: 0; }
  html, body {
    width: 1200px;
    height: 856px;
    overflow: hidden;
    background: var(--backdrop);
  }
  .card {
    position: absolute;
    left: 118px;
    top: 130px;
    width: 965px;
    height: 597px;
    background: var(--card);
    border-radius: 38px;
    overflow: hidden;
  }
  .plaid-band {
    position: absolute;
    left: 0;
    right: 0;
    top: 250px;
    bottom: 0;
    background:
      linear-gradient(to bottom,
        rgba(255,255,255,0) 0%,
        rgba(238,163,191,0.55) 22%,
        var(--rose) 52%,
        var(--maroon) 100%);
  }
  .lace-edge {
    position: absolute;
    left: 0;
    right: 0;
    bottom: 0;
    height: 150px;
    background: linear-gradient(to bottom, rgba(243,240,241,0) 0%, rgba(243,240,241,0.75) 35%, rgba(243,240,241,0.55) 100%);
  }
  .card-text {
    position: absolute;
    inset: 0;
    text-align: center;
    color: var(--ink);
  }
  .brand-name {
    position: absolute;
    left: 0; right: 0;
    top: 48px;
    font-family: "Parisienne", cursive;
    font-size: 64px;
    font-weight: 400;
    line-height: 1;
    color: var(--ink);
  }
  .tagline {
    position: absolute;
    left: 0; right: 0;
    top: 148px;
    font-family: "Italianno", cursive;
    font-size: 44px;
    line-height: 1;
    color: var(--pink);
  }
  .role {
    position: absolute;
    left: 0; right: 0;
    top: 228px;
    font-family: "Raleway", sans-serif;
    font-size: 26px;
    line-height: 1;
  }
  .person {
    position: absolute;
    left: 0; right: 0;
    top: 264px;
    font-family: "Raleway", sans-serif;
    font-weight: 700;
    font-size: 31px;
    line-height: 1;
    color: var(--pink);
  }
  .contact {
    position: absolute;
    left: 0; right: 0;
    font-family: "Raleway", sans-serif;
    font-size: 26px;
    line-height: 1;
    display: flex;
    justify-content: center;
    align-items: center;
    gap: 10px;
  }
  .contact-phone { top: 318px; }
  .contact-email { top: 356px; }
  .contact svg { display: block; }
</style>
</head>
<body>
  <div class="card">
    <div class="plaid-band" role="img" aria-label="Pink, white and maroon plaid pattern"></div>
    <div class="lace-edge" role="img" aria-label="White lace border"></div>
    <div class="card-text">
      <h1 class="brand-name">Cradlekin by Marianne</h1>
      <p class="tagline">Babies that never grow up</p>
      <p class="role">Reborn Artist</p>
      <p class="person">Marianne Holt</p>
      <p class="contact contact-phone">
        <svg width="16" height="24" viewBox="0 0 16 24" aria-hidden="true">
          <rect x="1.5" y="1.5" width="13" height="21" rx="2" fill="none" stroke="var(--pink)" stroke-width="2"/>
          <line x1="6" y1="19" x2="10" y2="19" stroke="var(--pink)" stroke-width="2"/>
        </svg>
        <span>0437 651 840</span>
      </p>
      <p class="contact contact-email">
        <svg width="26" height="18" viewBox="0 0 26 18" aria-hidden="true">
          <rect x="1" y="1" width="24" height="16" fill="none" stroke="var(--pink)" stroke-width="2"/>
          <polyline points="1,1 13,10 25,1" fill="none" stroke="var(--pink)" stroke-width="2"/>
        </svg>
        <span>lunet.v@mailvane.net</span>
      </p>
    </div>
  </div>
</body>
</html>
```